Eye catching business card

2 sided
Black background with logo in color on one side along with the words "Proudly serving the commercial and defense industries since 1975"
2nd side to contain contact information (see attached current business card) and "Waterjet, Composite, Precision Machining and Clean Room Manufacturing" with a very faint watermark of a waving USA Flag in the back ground.
Remove the "est. 195" from the current logo design

```html
<!DOCTYPE html>
<html lang="en">
<head>
<meta charset="utf-8">
<title>Meridian Fabrication — Business Card</title>
<link rel="stylesheet" href="https://fonts.googleapis.com/css2?family=Arimo:wght@400;700&display=swap">
<style>
  :root {
    --stage: #e6e7ea;
    --card: #1c2126;
    --card-edge: #262c32;
    --ink-light: #c9ccd0;
    --ink-muted: #8d9399;
    --accent: #2f8fe0;
    --accent-deep: #1f63c4;
  }
  * { box-sizing: border-box; margin: 0; padding: 0; }
  html, body { width: 1200px; height: 800px; overflow: hidden; }
  body {
    background: var(--stage);
    font-family: "Arimo", Arial, sans-serif;
    display: flex;
    align-items: center;
    justify-content: center;
    gap: 48px;
  }
  .card {
    position: relative;
    width: 540px;
    height: 309px;
    background: var(--card);
    border-radius: 18px;
    box-shadow: 0 10px 28px rgba(0,0,0,.22);
    overflow: hidden;
  }
  /* Front */
  .card--front {
    display: flex;
    flex-direction: column;
    align-items: center;
    justify-content: center;
    gap: 30px;
  }
  .brand {
    display: flex;
    align-items: center;
    gap: 14px;
  }
  .brand__mark {
    width: 30px;
    height: 30px;
    background: var(--accent);
  }
  .brand__name {
    color: var(--ink-light);
    font-weight: 700;
    font-size: 30px;
    letter-spacing: 1px;
    text-transform: uppercase;
  }
  .tagline {
    color: var(--ink-muted);
    font-size: 15px;
    letter-spacing: .3px;
    border-top: 1px solid #4a5057;
    padding-top: 14px;
  }
  /* Back */
  .card--back { padding: 34px 36px; }
  .back__brand {
    position: absolute;
    top: 54px;
    right: 36px;
    color: var(--accent);
    font-weight: 700;
    font-size: 44px;
    letter-spacing: 1px;
  }
  .contact {
    position: absolute;
    left: 36px;
    bottom: 36px;
    color: var(--ink-light);
    font-size: 12.5px;
    line-height: 1.55;
  }
  .contact__name {
    font-weight: 700;
    font-size: 17px;
    letter-spacing: .5px;
    text-transform: uppercase;
  }
  .contact__title {
    color: var(--accent);
    font-size: 14px;
    margin-bottom: 6px;
  }
  .contact__company {
    font-weight: 700;
    font-size: 15px;
    margin-top: 8px;
  }
  .contact__row { display: flex; align-items: center; gap: 7px; }
  .icon { width: 12px; height: 12px; fill: var(--accent); flex: none; }
  .contact__web { color: var(--accent); font-size: 14px; margin-top: 2px; }
  .services {
    color: var(--ink-muted);
    font-size: 12.5px;
    margin-top: 8px;
  }
</style>
</head>
<body>

<section class="card card--front" aria-label="Card front">
  <div class="brand">
    <span class="brand__mark"></span>
    <span class="brand__name">Meridian Fabrication</span>
  </div>
  <p class="tagline">Proudly serving the commercial and defense industries since 1975</p>
</section>

<section class="card card--back" aria-label="Card back">
  <div class="back__brand">MERIDIAN</div>
  <div class="contact">
    <p class="contact__name">Dale Whitford</p>
    <p class="contact__title">President</p>
    <p class="contact__row">
      <svg class="icon" viewBox="0 0 12 12"><path d="M2.4 0.8l2 2-1 1.4c.7 1.5 1.9 2.7 3.4 3.4l1.4-1 2 2-1.3 1.9C4.5 10.3 1.7 7.5 .5 2.1z"/></svg>
      555-014-0008
    </p>
    <p class="contact__row">
      <svg class="icon" viewBox="0 0 12 12"><path d="M0 2h12v8H0z M0 2l6 4.5L12 2" stroke="#1c2126" stroke-width="1"/></svg>
      dale@meridianfab.com
    </p>
    <p class="contact__company">Meridian Fabrication, Inc.</p>
    <p>412 North Ridge Rd. Fairview, PA 17000</p>
    <p class="contact__row">
      <svg class="icon" viewBox="0 0 12 12"><path d="M2.4 0.8l2 2-1 1.4c.7 1.5 1.9 2.7 3.4 3.4l1.4-1 2 2-1.3 1.9C4.5 10.3 1.7 7.5 .5 2.1z"/></svg>
      555-014-0008 &nbsp;|&nbsp;
      <svg class="icon" viewBox="0 0 12 12"><path d="M2 4h8v6H2z M3 1h6v3H3z"/></svg>
      555-014-0040
    </p>
    <p class="contact__row">
      <svg class="icon" viewBox="0 0 12 12"><path d="M0 2h12v8H0z M0 2l6 4.5L12 2" stroke="#1c2126" stroke-width="1"/></svg>
      info@meridianfab.com
    </p>
    <p class="contact__web">www.meridianfab.com</p>
    <p class="services">Waterjets | Composites | Precision Machining</p>
  </div>
</section>

</body>
</html>
```